We need an eye catching logo design and Business Card that portrays our business, which is the cleaning and protecting of stainless steel with an organic non chemical product. This can be separate to the company name or can incorporate it. Maybe even just the company name itself. Company Name is Gleamwise Gleamwise.
Ideal for products exposed to weather elements, ie: balustrading, enclosures, BBQs, we also supply the product so you can do it yourself (DIY).
In addition we would want to include on this card:
1. My Name (Paul Dremmick)
2. Mobile No. (TBA Later)
3. Email address (TBA Later)
4. Web address (TBA Later)
Updates

Please note that we also need suggestions on a logo, as this we do not have this either.

Please note we have update our brief to be more specific.

Thank You.

Paul

Reason: Awaiting for a couple of revised submissions from feedback given.

Target Market(s)

Purchasing officers and government people.

Industry/Entity Type

Steel

Colors

Designer to choose colors to be used in the design.

Requirements
Must have
• 1. Name (Paul Dremmick)
2. Mobile No. (TBA Later)
Should not have
• Should not be to busy looking

```html
<!DOCTYPE html>
<html lang="en">
<head>
<meta charset="utf-8">
<title>Gleamwise Gleamwise – Business Card</title>
<link href="https://fonts.googleapis.com/css2?family=Michroma&display=swap" rel="stylesheet">
<style>
  :root {
    --page: #ffffff;
    --ink: #2f5876;
    --steel-dark: #3f505c;
    --steel-mid: #8c9ba6;
    --steel-light: #dde3e8;
    --steel-bright: #ffffff;
    --band: rgba(255, 255, 255, 0.35);
  }
  * { margin: 0; padding: 0; box-sizing: border-box; }
  html, body {
    width: 900px;
    height: 1200px;
    overflow: hidden;
    background: var(--page);
  }
  .sheet {
    position: relative;
    width: 900px;
    height: 1200px;
    font-family: "Michroma", sans-serif;
    color: var(--ink);
  }
  .card {
    position: absolute;
    left: 121px;
    width: 659px;
    height: 401px;
    overflow: hidden;
    background:
      radial-gradient(ellipse 70% 80% at 55% 60%, rgba(255,255,255,0.9) 0%, rgba(255,255,255,0) 60%),
      linear-gradient(90deg,
        var(--steel-dark) 0%,
        var(--steel-mid) 18%,
        var(--steel-light) 38%,
        var(--steel-bright) 55%,
        var(--steel-light) 72%,
        var(--steel-mid) 88%,
        var(--steel-dark) 100%);
  }
  .card::after {
    content: "";
    position: absolute;
    inset: 0;
    background: linear-gradient(180deg, rgba(63,80,92,0.18) 0%, rgba(63,80,92,0) 25%, rgba(63,80,92,0) 80%, rgba(63,80,92,0.12) 100%);
    pointer-events: none;
  }
  .card--front { top: 150px; }
  .card--back { top: 623px; }
  .card__sheen {
    position: absolute;
    top: 0;
    left: 280px;
    width: 100px;
    height: 260px;
    background: linear-gradient(180deg, var(--band) 0%, rgba(255,255,255,0) 100%);
  }
  .brand-dot {
    position: absolute;
    left: 289px;
    top: 90px;
    width: 80px;
    height: 80px;
    border-radius: 50%;
    background: var(--ink);
  }
  .brand-name {
    position: absolute;
    left: 0;
    right: 0;
    top: 247px;
    text-align: center;
    font-size: 27px;
    letter-spacing: 0.5px;
    text-transform: uppercase;
    white-space: nowrap;
    color: var(--ink);
  }
  .contact-name,
  .contact-line {
    position: absolute;
    text-transform: uppercase;
    white-space: nowrap;
    text-shadow: 1px 2px 3px rgba(40, 60, 75, 0.35);
    z-index: 1;
  }
  .contact-name {
    left: 137px;
    top: 128px;
    font-size: 21px;
    letter-spacing: 1px;
  }
  .contact-line { left: 242px; }
  .contact-line--phone { top: 188px; font-size: 18px; letter-spacing: 1px; }
  .contact-line--email { top: 222px; font-size: 15px; }
  .contact-line--web { top: 252px; font-size: 15px; }
</style>
</head>
<body>
  <main class="sheet">
    <section class="card card--front" aria-label="Business card front">
      <div class="card__sheen"></div>
      <div class="brand-dot"></div>
      <h1 class="brand-name">Gleamwise Gleamwise</h1>
    </section>

    <section class="card card--back" aria-label="Business card back">
      <div class="card__sheen"></div>
      <h2 class="contact-name">Paul Dremmick</h2>
      <p class="contact-line contact-line--phone">0123 456 789</p>
      <p class="contact-line contact-line--email">pauldremmick@email.com</p>
      <p class="contact-line contact-line--web">www.website.com</p>
    </section>
  </main>
</body>
</html>
```